Brim-Vane PowerPoint Layout Design - Updated

We're now looking for a PowerPoint Layout design for Brim-Vane. Brim-Vane is an innovative, forward thinking insurance technology designed to help Commercially Focused Insurance Brokers and Agents track their organization's strategic performance and all of the individual opportunities that they come in contact with throughout a calendar year. Users gain powerful insights for improvement, efficiencies, and effectiveness that can be shared with their insurance carrier trading partners which, in turn, benefits their clients and the insurance professionals within these same organizations.

```html
<!DOCTYPE html>
<html lang="en">
<head>
<meta charset="utf-8">
<title>Brim-Vane Presentation Layout</title>
<link href="https://fonts.googleapis.com/css2?family=Mulish:wght@400;500;600;700;800&display=swap" rel="stylesheet">
<style>
:root{
  --backdrop:#c4c4c4;
  --paper:#ffffff;
  --green:#5a9a45;
  --yellow:#e2c15a;
  --ink:#2b2b2b;
  --body:#3f3f3f;
  --ring:#c9cbcb;
}
*{margin:0;padding:0;box-sizing:border-box}
html,body{width:1200px;height:1072px;overflow:hidden;background:var(--backdrop);font-family:'Mulish',sans-serif;color:var(--body)}
.board{position:relative;width:1200px;height:1072px}
.slide{position:absolute;width:544.6px;height:306.2px;background:var(--paper);overflow:hidden}
.col-a{left:37.7px}.col-b{left:617.8px}
.row-1{top:44.8px}.row-2{top:380.4px}.row-3{top:720.9px}
.abs{position:absolute}
.cityscape{position:absolute;inset:0;background:linear-gradient(180deg,#f6f6f6 0%,#ececec 45%,#e4e4e4 70%,#f0f0f0 100%)}
.slide-title{position:absolute;left:0;right:0;text-align:center;font-weight:600;color:var(--ink);font-size:22px;line-height:1}
.copy{font-size:7px;line-height:10.5px;color:var(--body);text-align:justify}
/* company name */
.brand-name{position:absolute;color:var(--ink);font-weight:600;white-space:nowrap;line-height:1}
.footer-brand{left:29px;top:283px;font-size:12px}
.cover-brand{left:0;right:0;top:136px;text-align:center;font-size:42px}
.copyright{position:absolute;left:274px;top:289px;font-size:5.4px;color:#555}
.socials{position:absolute;left:446px;top:286px;display:flex;gap:3.5px}
.socials span{width:12px;height:12px;border-radius:50%;background:#8e8e8e;display:block}
.page-no{position:absolute;left:506px;top:270px;width:29px;height:36.2px;background:var(--green);color:#fff;text-align:center}
.page-no small{display:block;font-size:3.6px;margin-top:10px;font-weight:600}
.page-no b{display:block;font-size:5.6px;margin-top:5px;font-weight:700}
/* about */
.about-title{left:32px;top:28px;font-size:23.5px;font-weight:600;color:var(--ink)}
.about-copy{left:32px;width:212px;font-size:6.9px}
.about-photo{position:absolute;left:272px;top:1px;width:276px;height:276px;border-radius:50%;background:radial-gradient(circle at 45% 55%,#b9a48f 0%,#8f7a66 40%,#6e5d50 70%,#9aa0a4 100%);box-shadow:0 0 6px rgba(0,0,0,.25)}
/* solutions */
.sol-text{position:absolute;width:150px;font-size:6.3px;line-height:9.4px;font-weight:600;color:var(--ink)}
.sol-text.left{left:70px;text-align:right}
.sol-text.right{left:325px}
.banner-label{position:absolute;color:#fff;font-weight:700;font-size:8.4px;width:140px;text-align:center}
/* infographic */
.info-block{position:absolute;width:130px}
.info-block h3{font-size:10.5px;font-weight:600;color:var(--ink);margin-bottom:4px}
.info-block p{font-size:7.2px;line-height:9.4px;color:var(--body)}
.info-block.left{left:64px;text-align:right}
.info-block.right{left:346px}
/* thank you */
.thanks{position:absolute;left:0;right:0;top:70px;text-align:center;font-size:31px;font-weight:700;color:var(--ink)}
.contact{position:absolute;width:110px;text-align:center;top:127px}
.contact .dot{width:28px;height:28px;border-radius:50%;background:var(--yellow);margin:0 auto;display:flex;align-items:center;justify-content:center}
.contact h4{font-size:7px;font-weight:800;color:var(--ink);margin-top:10px}
.contact p{font-size:7px;line-height:11px;color:var(--ink);margin-top:7px}
.divider{position:absolute;top:125px;width:0.6px;height:81px;background:#777}
</style>
</head>
<body>
<div class="board">

  <section class="slide col-a row-1">
    <div class="cityscape" role="img" aria-label="Faded photograph of a city skyline and plaza"></div>
    <div class="brand-name cover-brand">Brim-Vane</div>
  </section>

  <section class="slide col-b row-1">
    <h1 class="slide-title" style="top:29px">Our Mission</h1>
    <div class="abs copy" style="left:32px;top:81px;width:232px">
      <p>Lorem ipsum dolor sit amet, consectetur adipiscing elit, sed do eiusmod tempor incididunt ut labore et dolore magna aliqua. Ut enim ad minim veniam, quis nostrud exercitation ullamco laboris nisi ut aliquip ex ea commodo consequat. Duis aute irure dolor in reprehenderit in voluptate velit esse cillum dolore eu fugiat nulla pariatur. Excepteur sint occaecat cupidatat non proident, sunt in culpa qui officia deserunt mollit anim id est laborum.</p>
      <p style="margin-top:10.5px">Lorem ipsum dolor sit amet, consectetur adipiscing elit, sed do eiusmod tempor incididunt ut labore et dolore magna aliqua. Ut enim ad minim veniam, quis nostrud exercitation ullamco laboris nisi ut aliquip ex ea commodo consequat. Duis aute irure dolor in reprehenderit in voluptate velit esse cillum dolore eu fugiat nulla pariatur. Excepteur sint occaecat cupidatat non proident, sunt in culpa qui officia deserunt mollit anim id est laborum.</p>
    </div>
    <div class="abs copy" style="left:281px;top:81px;width:232px">
      <p>Lorem ipsum dolor sit amet, consectetur adipiscing elit, sed do eiusmod tempor incididunt ut labore et dolore magna aliqua. Ut enim ad minim veniam, quis nostrud exercitation ullamco laboris nisi ut aliquip ex ea commodo consequat. Duis aute irure dolor in reprehenderit in voluptate velit esse cillum dolore eu fugiat nulla pariatur. Excepteur sint occaecat cupidatat non proident, sunt in culpa qui officia deserunt mollit anim id est laborum.</p>
      <p style="margin-top:10.5px">Lorem ipsum dolor sit amet, consectetur adipiscing elit, sed do eiusmod tempor incididunt ut labore et dolore magna aliqua. Ut enim ad minim veniam, quis nostrud exercitation ullamco laboris nisi ut aliquip ex ea commodo consequat. Duis aute irure dolor in reprehenderit in voluptate velit esse cillum dolore eu fugiat nulla pariatur. Excepteur sint occaecat cupidatat non proident, sunt in culpa qui officia deserunt mollit anim id est laborum.</p>
    </div>
    <div class="brand-name footer-brand">Brim-Vane</div>
    <div class="copyright">© Copyrights 2024 Company name . All rights reserved</div>
    <div class="socials"><span></span><span></span><span></span></div>
    <div class="page-no"><small>Page No :</small><b>04</b></div>
  </section>

  <section class="slide col-a row-2">
    <h1 class="abs about-title">About Us</h1>
    <div class="abs copy about-copy" style="top:63.6px">Lorem ipsum dolor sit amet, consectetur adipiscing elit, sed do eiusmod tempor incididunt ut labore et dolore magna aliqua. Ut enim ad minim veniam, quis nostrud exercitation ullamco laboris nisi ut aliquip ex ea commodo consequat. Duis aute irure dolor in reprehenderit in voluptate velit esse cillum dolore eu fugiat nulla pariatur. Excepteur sint occaecat cupidatat non proident, sunt in culpa qui officia deserunt mollit anim id est laborum.</div>
    <div class="abs copy about-copy" style="top:148px">Lorem ipsum dolor sit amet, consectetur adipiscing elit, sed do eiusmod tempor incididunt ut labore et dolore magna aliqua. Ut enim ad minim veniam, quis nostrud exercitation ullamco laboris nisi ut aliquip ex ea commodo consequat. Duis aute irure dolor in reprehenderit in voluptate velit esse cillum dolore eu fugiat nulla pariatur. Excepteur sint occaecat cupidatat non proident, sunt in culpa qui officia deserunt mollit anim id est laborum.</div>
    <div class="about-photo" role="img" aria-label="Photograph of a team meeting around a wooden table with laptops and papers"></div>
    <svg class="abs" style="left:0;top:0" width="545" height="306" viewBox="0 0 545 306" aria-hidden="true">
      <circle cx="422" cy="123" r="100" fill="none" stroke="var(--ring)" stroke-width="9" opacity=".95"/>
      <circle cx="422" cy="123" r="56" fill="none" stroke="var(--ring)" stroke-width="9" opacity=".95"/>
    </svg>
    <div class="brand-name footer-brand">Brim-Vane</div>
    <div class="copyright">© Copyrights 2024 Company name . All rights reserved</div>
    <div class="socials"><span></span><span></span><span></span></div>
    <div class="page-no"><small>Page No :</small><b>02</b></div>
  </section>

  <section class="slide col-b row-2">
    <h1 class="slide-title" style="top:29px">Solutions</h1>
    <svg class="abs" style="left:0;top:0" width="545" height="306" viewBox="0 0 545 306">
      <defs>
        <linearGradient id="solPhoto" x1="0" y1="0" x2="1" y2="1">
          <stop offset="0" stop-color="#e9e7e3"/><stop offset=".5" stop-color="#b9a792"/><stop offset="1" stop-color="#6f7b86"/>
        </linearGradient>
      </defs>
      <g fill="var(--green)">
        <polygon points="89,118 101,106 254,106 230,130 101,130"/>
        <polygon points="290,106 444,106 456,118 444,130 314,130"/>
        <polygon points="89,187 101,175 230,175 254,199 101,199"/>
        <polygon points="314,175 444,175 456,187 444,199 290,199"/>
      </g>
      <g fill="var(--yellow)">
        <polygon points="242.5,71 255,79 255,99 242.5,107 230,99 230,79"/>
        <polygon points="301.5,71 314,79 314,99 301.5,107 289,99 289,79"/>
        <polygon points="242.5,198 255,206 255,226 242.5,234 230,226 230,206"/>
        <polygon points="301.5,198 314,206 314,226 301.5,234 289,226 289,206"/>
      </g>
      <g fill="none" stroke="#fff" stroke-width="1.4" stroke-linecap="round" stroke-linejoin="round">
        <path d="M237 89l4 4 7-8"/>
        <rect x="296" y="83" width="11" height="12" rx="1.5"/><path d="M298.5 89l2 2 4-4"/>
        <circle cx="242.5" cy="209" r="2"/><path d="M236 213l6.5 3 6.5-3M242.5 216v9M239 227l3.5-4 3.5 4"/>
        <circle cx="301.5" cy="216" r="6.5"/><path d="M301.5 212v4l3 2"/>
      </g>
      <polygon points="273,103 320,150 273,197 226,150" fill="url(#solPhoto)" role="img" aria-label="Photograph of two colleagues working together at a desk"/>
    </svg>
    <div class="banner-label" style="left:100px;top:113px">Lorem ipsum dolor sit amet</div>
    <div class="banner-label" style="left:305px;top:113px">Lorem ipsum dolor sit amet</div>
    <div class="banner-label" style="left:100px;top:182px">Lorem ipsum dolor sit amet</div>
    <div class="banner-label" style="left:305px;top:182px">Lorem ipsum dolor sit amet</div>
    <p class="sol-text left" style="top:62px">Lorem ipsum dolor sit amet, consectetur adipiscing elit, sed do eiusmod tempor incididunt ut labore et dolore magna aliqua. Ut enim ad niam, quis nostrud exercitation ullamco</p>
    <p class="sol-text right" style="top:62px">Lorem ipsum dolor sit amet, consectetur adipiscing elit, sed do eiusmod tempor incididunt ut labore et dolore magna aliqua. Ut enim ad niam, quis nostrud exercitation ullamco</p>
    <p class="sol-text left" style="top:204px">Lorem ipsum dolor sit amet, consectetur adipiscing elit, sed do eiusmod tempor incididunt ut labore et dolore magna aliqua. Ut enim ad niam, quis nostrud exercitation ullamco</p>
    <p class="sol-text right" style="top:204px">Lorem ipsum dolor sit amet, consectetur adipiscing elit, sed do eiusmod tempor incididunt ut labore et dolore magna aliqua. Ut enim ad niam, quis nostrud exercitation ullamco</p>
    <div class="brand-name footer-brand">Brim-Vane</div>
    <div class="copyright">© Copyrights 2024 Company name . All rights reserved</div>
    <div class="socials"><span></span><span></span><span></span></div>
    <div class="page-no"><small>Page No :</small><b>05</b></div>
  </section>

  <section class="slide col-a row-3">
    <h1 class="slide-title" style="top:29px">InfoGraphic</h1>
    <svg class="abs" style="left:0;top:0" width="545" height="306" viewBox="0 0 545 306" aria-hidden="true">
      <g fill="none" stroke="var(--green)" stroke-width="1.2">
        <circle cx="237" cy="104" r="29"/><circle cx="308" cy="104" r="29"/>
        <circle cx="237" cy="186" r="29"/><circle cx="308" cy="186" r="29"/>
      </g>
      <g fill="var(--yellow)">
        <circle cx="237" cy="104" r="25"/><circle cx="308" cy="104" r="25"/>
        <circle cx="237" cy="186" r="25"/><circle cx="308" cy="186" r="25"/>
      </g>
      <g fill="#fff">
        <rect x="233" y="92" width="10" height="7" rx="1"/>
        <circle cx="231" cy="105" r="2.4"/><circle cx="243" cy="105" r="2.4"/>
        <path d="M226 114a5 5 0 0 1 10 0zM238 114a5 5 0 0 1 10 0z"/>
        <circle cx="309" cy="99" r="4.5"/>
        <path d="M297 107h8l6 3h6l-2 4h-18z"/>
        <rect x="226" y="177" width="18" height="13" rx="1.5"/>
        <circle cx="312" cy="178" r="2.5"/><circle cx="304" cy="178" r="2.5"/>
        <rect x="300" y="188" width="16" height="2"/>
      </g>
      <circle cx="309" cy="99" r="2" fill="var(--yellow)"/>
      <circle cx="235" cy="183.5" r="3" fill="var(--yellow)"/>
      <path d="M303 183v10M313 183v10M302 195v3M314 195v3" stroke="#fff" stroke-width="1.6"/>
    </svg>
    <div class="info-block left" style="top:76px"><h3>Duis aute irure dolor</h3><p>Lorem ipsum dolor sit amet, consectetur adipiscing elit, sed do eiusmod tempor incididunt ut labore et dolore magna aliqua.</p></div>
    <div class="info-block right" style="top:76px"><h3>Duis aute irure dolor</h3><p>Lorem ipsum dolor sit amet, consectetur adipiscing elit, sed do eiusmod tempor incididunt ut labore et dolore magna aliqua.</p></div>
    <div class="info-block left" style="top:158px"><h3>Duis aute irure dolor</h3><p>Lorem ipsum dolor sit amet, consectetur adipiscing elit, sed do eiusmod tempor incididunt ut labore et dolore magna aliqua.</p></div>
    <div class="info-block right" style="top:158px"><h3>Duis aute irure dolor</h3><p>Lorem ipsum dolor sit amet, consectetur adipiscing elit, sed do eiusmod tempor incididunt ut labore et dolore magna aliqua.</p></div>
    <div class="brand-name footer-brand">Brim-Vane</div>
    <div class="copyright">© Copyrights 2024 Company name . All rights reserved</div>
    <div class="socials"><span></span><span></span><span></span></div>
    <div class="page-no"><small>Page No :</small><b>03</b></div>
  </section>

  <section class="slide col-b row-3">
    <div class="cityscape" role="img" aria-label="Faded photograph of a city skyline and plaza"></div>
    <h1 class="thanks">Thank You</h1>
    <div class="contact" style="left:100px">
      <div class="dot"><svg width="10" height="12" viewBox="0 0 10 12"><path d="M5 0a4 4 0 0 1 4 4c0 3-4 8-4 8S1 7 1 4a4 4 0 0 1 4-4z" fill="#fff"/><circle cx="5" cy="4" r="1.5" fill="var(--yellow)"/></svg></div>
      <h4>ADDRESS:</h4><p>123,Lorem ipsum dolor sit<br>amet, consectetur</p>
    </div>
    <div class="divider" style="left:223px"></div>
    <div class="contact" style="left:218px">
      <div class="dot"><svg width="11" height="11" viewBox="0 0 11 11"><path d="M2.5 0.5l2 2.5-1.3 1.4a7 7 0 0 0 3.4 3.4L8 6.5l2.5 2-1.2 2C5 10.5 0.5 6 0.5 1.7z" fill="#fff"/></svg></div>
      <h4>PHONE:</h4><p>+1 888 888 8888</p>
    </div>
    <div class="divider" style="left:329px"></div>
    <div class="contact" style="left:335px">
      <div class="dot"><svg width="12" height="9" viewBox="0 0 12 9"><rect width="12" height="9" rx="1" fill="#fff"/><path d="M0.5 1l5.5 4 5.5-4" fill="none" stroke="var(--yellow)" stroke-width="1"/></svg></div>
      <h4>EMAIL ADDRESS:</h4><p>info@brimvanemail.com</p>
    </div>
    <div class="brand-name footer-brand">Brim-Vane</div>
    <div class="copyright">© Copyrights 2024 Company name . All rights reserved</div>
    <div class="socials"><span></span><span></span><span></span></div>
    <div class="page-no"><small>Page No :</small><b>06</b></div>
  </section>

</div>
</body>
</html>
```